Business Card - connecting 2 souls and beggining the journey of self discovery

Logo on the front
with tag line

On the back list of services and contact details

Seminars
workshops
Coaching
podcasts

Daniel Porthwick
Health & Wellbeing Life Coach
0491 372 815
daniel@wovenpathwellness.example
wovenpathwellness.example

Industry/Entity Type

Life Coaching

Contact Information for Business Card

I like the use of colour from the logo to be used. I'm not a fan of white.

Requirements
Must have
• My tagline: The journey home starts with you
Nice to have
• Use of colour that is in the mind body soul logo

```html
<!DOCTYPE html>
<html lang="en">
<head>
<meta charset="utf-8">
<title>Woven Path Wellness – Business Card</title>
<link href="https://fonts.googleapis.com/css2?family=Lato:wght@400;700&family=Mulish:wght@500;600&display=swap" rel="stylesheet">
<style>
  :root{
    --stage:#e6e6e8;
    --purple:#7a3f97;
    --purple-deep:#5c2d7e;
    --violet-sky:#8a4a9c;
    --rose:#b86a7e;
    --amber:#e69a3a;
    --gold:#f2cc38;
    --tan:#d9b27a;
    --white:#ffffff;
    --ink:#4a4a4a;
    --ink-soft:#666666;
    --icon-ring:#f3f3f3;
  }
  *{box-sizing:border-box;margin:0;padding:0}
  html,body{width:1200px;height:723px;overflow:hidden}
  body{background:var(--stage);font-family:'Lato',sans-serif;position:relative}

  .card{position:absolute;top:201px;width:540px;height:320px;overflow:hidden;
        box-shadow:0 6px 18px rgba(0,0,0,.22)}
  .card--front{left:40px}
  .card--back{left:620px;background:var(--white)}

  /* front */
  .front-scene{position:absolute;inset:0;
    background:linear-gradient(180deg,var(--violet-sky) 0%,var(--rose) 38%,var(--amber) 72%,var(--gold) 100%)}
  .front-mark{position:absolute;left:222px;top:63px;width:90px;height:90px;border-radius:50%;
    background:var(--white);opacity:.85}
  .front-name{position:absolute;left:0;right:0;top:193px;text-align:center;color:var(--white);
    font-family:'Mulish',sans-serif;font-weight:600;font-size:26px;letter-spacing:-.5px}
  .front-tagline{position:absolute;left:0;right:0;top:246px;text-align:center;color:var(--white);
    font-family:'Mulish',sans-serif;font-weight:500;font-size:19px}

  /* back */
  .back-top-band{position:absolute;left:0;top:0;width:100%;height:88px;
    background:linear-gradient(90deg,var(--rose) 0%,var(--tan) 55%,var(--gold) 100%)}
  .back-bottom-band{position:absolute;left:0;bottom:0;width:100%;height:33px;
    background:linear-gradient(90deg,var(--purple) 0%,var(--rose) 50%,var(--tan) 100%)}
  .services{position:absolute;top:38px;left:26px;right:26px;display:flex;justify-content:space-between}
  .service{width:110px;display:flex;flex-direction:column;align-items:center}
  .service-icon{width:60px;height:60px;border-radius:50%;background:var(--white);
    border:2px solid var(--icon-ring);display:flex;align-items:center;justify-content:center}
  .service-icon svg{width:34px;height:34px}
  .service-label{margin-top:10px;font-family:'Mulish',sans-serif;font-weight:500;font-size:18px;color:var(--ink)}

  .brand{position:absolute;left:30px;top:160px;width:220px;display:flex;flex-direction:column;align-items:center}
  .brand-mark{width:66px;height:66px;border-radius:50%;background:var(--purple)}
  .brand-name{margin-top:14px;font-family:'Mulish',sans-serif;font-weight:500;font-size:15px;color:var(--ink)}

  .contact{position:absolute;left:284px;top:162px}
  .contact-name{font-weight:700;font-size:15px;color:var(--purple)}
  .contact-role{font-size:13.5px;color:var(--ink);margin-top:2px}
  .contact-list{list-style:none;margin-top:20px}
  .contact-item{display:flex;align-items:center;gap:8px;font-size:13px;color:var(--ink-soft);line-height:18px}
  .contact-item svg{width:11px;height:11px;flex:none}
</style>
</head>
<body>

<section class="card card--front" aria-label="Business card front">
  <div class="front-scene" role="img" aria-label="Photo of two raised open hands against a purple and golden sunset sky"></div>
  <div class="front-mark"></div>
  <h1 class="front-name">Woven Path Wellness</h1>
  <p class="front-tagline">The journey home starts with you</p>
</section>

<section class="card card--back" aria-label="Business card back">
  <div class="back-top-band"></div>

  <ul class="services">
    <li class="service">
      <span class="service-icon">
        <svg viewBox="0 0 34 34" fill="none" stroke="var(--purple)" stroke-width="2.4">
          <rect x="6" y="5" width="22" height="16" rx="1"/>
          <path d="M17 21v8M11 29h12"/>
        </svg>
      </span>
      <span class="service-label">Seminars</span>
    </li>
    <li class="service">
      <span class="service-icon">
        <svg viewBox="0 0 34 34" fill="var(--purple)">
          <path d="M17 6c4 4 4 10 0 16c-4-6-4-12 0-16z"/>
          <path d="M5 14c6 0 10 4 11 9c-6 0-10-3-11-9zM29 14c-6 0-10 4-11 9c6 0 10-3 11-9z"/>
          <rect x="6" y="25" width="22" height="3" rx="1.5"/>
        </svg>
      </span>
      <span class="service-label">Workshops</span>
    </li>
    <li class="service">
      <span class="service-icon">
        <svg viewBox="0 0 34 34" fill="var(--purple)">
          <rect x="8" y="14" width="18" height="3" rx="1"/>
          <rect x="16" y="17" width="2" height="10"/>
          <rect x="3" y="9" width="4" height="18" rx="1"/>
          <rect x="27" y="9" width="4" height="18" rx="1"/>
        </svg>
      </span>
      <span class="service-label">Coaching</span>
    </li>
    <li class="service">
      <span class="service-icon">
        <svg viewBox="0 0 34 34" fill="none" stroke="var(--purple)" stroke-width="2.4" stroke-linecap="round">
          <path d="M9 24a11 11 0 1 1 16 0"/>
          <path d="M12.5 20.5a6 6 0 1 1 9 0"/>
          <circle cx="17" cy="15" r="2.4" fill="var(--purple)" stroke="none"/>
          <path d="M17 19v10"/>
        </svg>
      </span>
      <span class="service-label">Podcasts</span>
    </li>
  </ul>

  <div class="brand">
    <span class="brand-mark"></span>
    <span class="brand-name">Woven Path Wellness</span>
  </div>

  <div class="contact">
    <p class="contact-name">Daniel Porthwick</p>
    <p class="contact-role">Health &amp; Wellbeing Life Coach</p>
    <ul class="contact-list">
      <li class="contact-item">
        <svg viewBox="0 0 12 12" fill="var(--purple)"><path d="M2.5 1l2 2.2-1 1.3a7 7 0 0 0 4 4l1.3-1L11 9.5 9.6 11C5 10.6 1.4 7 1 2.4z"/></svg>
        0491 372 815
      </li>
      <li class="contact-item">
        <svg viewBox="0 0 12 12" fill="none" stroke="var(--purple)" stroke-width="1.4"><rect x="1" y="2.5" width="10" height="7"/><path d="M1 2.5l5 4 5-4"/></svg>
        daniel@wovenpathwellness.example
      </li>
      <li class="contact-item">
        <svg viewBox="0 0 12 12" fill="none" stroke="var(--purple)" stroke-width="1.2"><circle cx="6" cy="6" r="5"/><ellipse cx="6" cy="6" rx="2.2" ry="5"/><path d="M1 6h10"/></svg>
        wovenpathwellness.example
      </li>
    </ul>
  </div>

  <div class="back-bottom-band"></div>
</section>

</body>
</html>
```